Shine4all

Full service cleaning company. Specializing in commercial and apartment cleans.
Fully licensed and insured
Digital photos and invoices provided
for every job
For web designer...basic info as expected by a highend cleaning company that provides excellent service at reasonable pricing. We are going after large property management companies as well as not pricing ourselves out to help the local mom and pop companies as well.
Updates

Project Deadline Extended Reason: Everyone seems to be having trouble understanding that we are a dumpster company that is adding a cleaning side to the company. We want our clients to see Shine4All as a separate branch of our our already established waste management company.We are not a regular cleaning company. We specialize in going after large commercial cleans and apartment cleans. I have now included info regarding a proposal for work and our invoice/job completion to make it clearer what we do Added Monday, July 20, 2015

Target Market(s)

Property Management companies in Savannah, Richmond Hill, Rincon, Hinesville and Midway Georgia

Industry/Entity Type

Cleaning Service

Coding

Coded - Design and coding required

Number of Pages Required

3 page

Requirements
Must have
• Nice home page with lots of photos (stock are fine) to convey exactly what we do (getting logo bid on right now on this sight).
• Information page with employee photos (can leave blank) need room for 4 photos and bios.
• Page or link to a static page for the dumpster company BinTrek (logo for this is red and black file attached along with photo of dumpster. This page just needs to be one page with contact info and information about commercial dumpster.
• Basically this site is just a fluff page used for marketing purposes. Its content can be general and once created wont change much. Services and photos can be provided upon request but general layout and info is what we are looking for.

```html
<!DOCTYPE html>
<html lang="en">
<head>
<meta charset="utf-8">
<title>Shine4All – Commercial &amp; Apartment Cleaning</title>
<link href="https://fonts.googleapis.com/css2?family=Oswald:wght@400;500;700&family=Open+Sans:wght@400;600;700&display=swap" rel="stylesheet">
<style>
:root{
  --red:#e3111b;
  --red-dark:#b80d15;
  --black:#111;
  --dark:#1c1c1c;
  --footer:#202020;
  --text:#444;
  --muted:#888;
  --line:#ddd;
  --white:#fff;
}
*{box-sizing:border-box;margin:0;padding:0}
html,body{width:726px;height:1200px;overflow:hidden}
body{font-family:"Open Sans",Arial,sans-serif;color:var(--text);background:var(--white);font-size:7px;line-height:1.5}
h1,h2,h3,h4{font-family:"Oswald",Arial,sans-serif;font-weight:500;color:var(--black)}
.wrap{width:680px;margin:0 auto;position:relative}

/* header */
.site-header{height:64px}
.site-header .wrap{height:64px;display:flex;align-items:flex-end;justify-content:space-between}
.brand{display:flex;align-items:center;gap:6px;align-self:center;font-family:"Oswald",Arial,sans-serif;font-weight:700;font-size:22px;color:var(--red)}
.brand-dot{width:14px;height:14px;border-radius:50%;background:var(--red)}
.top-phone{position:absolute;right:0;top:6px;display:flex;align-items:center;gap:4px;font-family:"Oswald",Arial,sans-serif;font-size:11px;color:var(--red)}
.main-nav{display:flex;margin-bottom:8px}
.main-nav a{font-family:"Oswald",Arial,sans-serif;font-size:9.5px;color:var(--black);text-decoration:none;padding:12px 11px;border-left:1px solid var(--line)}
.main-nav a.active{background:var(--black);color:var(--white);border-left:none}

/* hero */
.hero{height:296px;position:relative}
.hero-photo{position:absolute;inset:0;background:linear-gradient(100deg,#5c6a4f 0%,#7c8a78 30%,#9aa6a8 55%,#4d5560 80%,#3a3f46 100%)}
.hero-copy{position:absolute;left:410px;top:150px;color:var(--white)}
.hero-copy h1{color:var(--white);font-size:21px;font-weight:700;line-height:1.15}
.hero-copy p{font-family:"Oswald",Arial,sans-serif;font-size:19px;font-weight:700;line-height:1.2;margin-top:10px}

/* welcome + form */
.intro{height:240px;padding-top:24px}
.intro .wrap{display:flex;justify-content:space-between}
.welcome{width:400px}
.section-title{font-size:17px;position:relative;padding-bottom:7px;margin-bottom:10px}
.section-title::after{content:"";position:absolute;left:0;bottom:0;width:44px;height:2px;background:var(--red)}
.welcome p{margin-bottom:9px;font-size:7.5px}
.btn{display:inline-block;background:var(--red);color:var(--white);font-family:"Oswald",Arial,sans-serif;font-size:8px;padding:5px 10px;text-decoration:none}
.schedule{width:236px}
.schedule .field{border:1px solid #ccc;height:18px;margin-bottom:6px;font-size:6.5px;color:var(--muted);padding:4px 6px}
.schedule .row{display:flex;gap:6px}
.schedule .row .field{flex:1}
.schedule .field.message{height:40px}

/* audience band */
.audience{height:170px;background:var(--dark)}
.audience .wrap{display:flex;justify-content:space-between;padding-top:26px}
.audience-card{width:210px}
.audience-photo{height:100px;position:relative}
.audience-photo span{position:absolute;left:0;bottom:10px;background:var(--red);color:var(--white);font-family:"Oswald",Arial,sans-serif;font-size:10px;padding:2px 8px}
.home-photo{background:linear-gradient(135deg,#6d7b8c,#b9a98c 60%,#5a4a3c)}
.business-photo{background:linear-gradient(135deg,#7b8d9c,#3b6b3a 55%,#2e3a2c)}
.rent-photo{background:linear-gradient(135deg,#d9dde0,#a83b34 55%,#5c1f1b)}
.audience-card a{display:block;color:#ccc;font-size:6.5px;margin-top:4px;text-decoration:none}

/* features */
.features{height:215px;padding-top:18px}
.features .wrap{display:flex;justify-content:space-between}
.feature{width:210px}
.feature h3{font-size:16px;font-weight:700;margin-bottom:10px}
.feature-photo{height:80px;margin-bottom:6px}
.access-photo{background:linear-gradient(135deg,#2b2f36,#8a929c 50%,#1f2228)}
.bins-photo{background:linear-gradient(180deg,#b6c6cf,#4f9a3c 55%,#2f6a26)}
.feature p{font-size:7px}
.why-list{list-style:none}
.why-list li{display:flex;align-items:center;gap:6px;font-size:7.5px;padding:3px 0}

/* cta */
.cta{height:45px;background:var(--red)}
.cta .wrap{display:flex;align-items:center;height:45px;gap:14px}
.cta h4{color:var(--white);font-size:11px;font-weight:500}
.cta .zip{background:var(--white);width:116px;height:18px;font-size:6.5px;color:var(--muted);padding:4px 6px}
.cta .btn{background:var(--black);font-size:7.5px}

/* footer */
.site-footer{height:145px;background:var(--footer);color:#bbb}
.site-footer .wrap{display:flex;padding-top:18px}
.site-footer h4{color:var(--white);font-size:10.5px;margin-bottom:8px}
.quick-links{width:120px}
.quick-links li,.faq li{list-style:none;font-size:6.5px;padding:1px 0}
.quick-links li::before,.faq li::before{content:"› ";color:var(--red)}
.contact-info{width:160px}
.contact-info p{display:flex;gap:5px;font-size:6.5px;margin-bottom:6px;align-items:flex-start}
.faq{width:180px}
.faq .more{color:var(--white);font-size:6.5px;margin-top:3px;display:block}
.footer-brand{flex:1;display:flex;align-items:center;justify-content:flex-end;gap:6px;font-family:"Oswald",Arial,sans-serif;font-weight:700;font-size:22px;color:#aaa;padding-top:30px}
.footer-brand .brand-dot{background:#aaa}
.bottom-bar{height:25px;background:var(--black);color:#999;font-size:6.5px}
.bottom-bar .wrap{display:flex;align-items:center;justify-content:space-between;height:25px}
.social{display:flex;gap:4px}
.social span{width:12px;height:12px;background:#555}
</style>
</head>
<body>

<header class="site-header">
  <div class="wrap">
    <div class="brand"><span class="brand-dot"></span>Shine4All</div>
    <div class="top-phone">
      <svg width="9" height="9" viewBox="0 0 24 24"><path fill="#e3111b" d="M6.6 10.8a15.1 15.1 0 0 0 6.6 6.6l2.2-2.2c.3-.3.7-.4 1-.2 1.1.4 2.3.6 3.6.6.6 0 1 .4 1 1V20c0 .6-.4 1-1 1A17 17 0 0 1 3 4c0-.6.4-1 1-1h3.5c.6 0 1 .4 1 1 0 1.3.2 2.5.6 3.6.1.3 0 .7-.2 1z"/></svg>
      555 014 2318
    </div>
    <nav class="main-nav">
      <a class="active" href="#">Home</a>
      <a href="#">About Us</a>
      <a href="#">Services</a>
      <a href="#">Think Green</a>
      <a href="#">Customer Reviews</a>
      <a href="#">Contact Us</a>
    </nav>
  </div>
</header>

<section class="hero">
  <div class="hero-photo" role="img" aria-label="Green waste truck lifting a dumpster beside tall apartment buildings"></div>
  <div class="hero-copy">
    <h1>We Are A full Service<br>Cleaning Company</h1>
    <p>Specializing in commercial<br>and apartment cleans</p>
  </div>
</section>

<section class="intro">
  <div class="wrap">
    <div class="welcome">
      <h2 class="section-title">Welcome To Shine4All</h2>
      <p>Lorem ipsum dolor sit amet, consectetuer adipiscing elit, sed diam nonummy nibh euismod tincidunt ut laoreet dolore magna aliquam erat volutpat. Ut wisi enim ad minim veniam, quis nostrud exerci tation ullamcorper suscipit lobortis nisl ut aliquip ex ea commodo consequat.</p>
      <p>Duis autem vel eum iriure dolor in hendrerit in vulputate velit esse molestie consequat, vel illum dolore eu feugiat nulla facilisis.</p>
      <a class="btn" href="#">READ MORE</a>
    </div>
    <form class="schedule">
      <h2 class="section-title">Schedule A Service</h2>
      <div class="field">Name</div>
      <div class="field">Phone</div>
      <div class="row">
        <div class="field">Pick up Date &amp; Time</div>
        <div class="field">Date</div>
        <div class="field">Time</div>
      </div>
      <div class="field message">Message</div>
      <a class="btn" href="#">SUBMIT</a>
    </form>
  </div>
</section>

<section class="audience">
  <div class="wrap">
    <div class="audience-card">
      <div class="audience-photo home-photo" role="img" aria-label="Dumpster in front of a family home"><span>Home Owner</span></div>
      <a href="#">Read More »</a>
    </div>
    <div class="audience-card">
      <div class="audience-photo business-photo" role="img" aria-label="Waste truck serving a business site"><span>Business Owner</span></div>
      <a href="#">Read More »</a>
    </div>
    <div class="audience-card">
      <div class="audience-photo rent-photo" role="img" aria-label="Red roll-off dumpster ready to rent"><span>Rent-a-Dumpster</span></div>
      <a href="#">Read More »</a>
    </div>
  </div>
</section>

<section class="features">
  <div class="wrap">
    <div class="feature">
      <h3>24/7 Access</h3>
      <div class="feature-photo access-photo" role="img" aria-label="24 hour service sign"></div>
      <p>Lorem ipsum dolor sit amet consectetuer adipiscing elit sed diam nonummy nibh euismod.</p>
    </div>
    <div class="feature">
      <h3>Reliable. Clean. Safe.</h3>
      <div class="feature-photo bins-photo" role="img" aria-label="Row of green waste bins"></div>
      <p>Lorem ipsum dolor sit amet consectetuer adipiscing elit sed diam nonummy nibh euismod.</p>
    </div>
    <div class="feature">
      <h3>Why Choos Us</h3>
      <ul class="why-list">
        <li><svg width="8" height="8" viewBox="0 0 10 10"><path d="M1 5l3 3 5-6" stroke="#e3111b" stroke-width="1.8" fill="none"/></svg>Wide selection of dumpster sizes available</li>
        <li><svg width="8" height="8" viewBox="0 0 10 10"><path d="M1 5l3 3 5-6" stroke="#e3111b" stroke-width="1.8" fill="none"/></svg>Flexible, Timely pickup and delivery</li>
        <li><svg width="8" height="8" viewBox="0 0 10 10"><path d="M1 5l3 3 5-6" stroke="#e3111b" stroke-width="1.8" fill="none"/></svg>Fresh service available</li>
        <li><svg width="8" height="8" viewBox="0 0 10 10"><path d="M1 5l3 3 5-6" stroke="#e3111b" stroke-width="1.8" fill="none"/></svg>Easy online ordering and scheduling</li>
        <li><svg width="8" height="8" viewBox="0 0 10 10"><path d="M1 5l3 3 5-6" stroke="#e3111b" stroke-width="1.8" fill="none"/></svg>Online account management</li>
        <li><svg width="8" height="8" viewBox="0 0 10 10"><path d="M1 5l3 3 5-6" stroke="#e3111b" stroke-width="1.8" fill="none"/></svg>Instant online pricing</li>
      </ul>
    </div>
  </div>
</section>

<section class="cta">
  <div class="wrap">
    <h4>Ready To Get Started? See What Dumpsters Are Available In Your Area.</h4>
    <div class="zip">Enter Zip Code or Post Code</div>
    <a class="btn" href="#">SHOW PRODUCTS</a>
  </div>
</section>

<footer class="site-footer">
  <div class="wrap">
    <div class="quick-links">
      <h4>Quick Links</h4>
      <ul>
        <li>Home</li><li>About Us</li><li>Services</li><li>Think Green</li><li>Customer Reviews</li><li>Contact Us</li>
      </ul>
    </div>
    <div class="contact-info">
      <h4>Contact Information</h4>
      <p><svg width="8" height="9" viewBox="0 0 24 24"><path fill="#e3111b" d="M12 2a7 7 0 0 0-7 7c0 5 7 13 7 13s7-8 7-13a7 7 0 0 0-7-7zm0 9.5A2.5 2.5 0 1 1 12 6a2.5 2.5 0 0 1 0 5.5z"/></svg>1234 Harbor Street, Suite 5,<br>Savannah, GA 31401</p>
      <p><svg width="8" height="8" viewBox="0 0 24 24"><path fill="#e3111b" d="M6.6 10.8a15.1 15.1 0 0 0 6.6 6.6l2.2-2.2c.3-.3.7-.4 1-.2 1.1.4 2.3.6 3.6.6.6 0 1 .4 1 1V20c0 .6-.4 1-1 1A17 17 0 0 1 3 4c0-.6.4-1 1-1h3.5c.6 0 1 .4 1 1 0 1.3.2 2.5.6 3.6.1.3 0 .7-.2 1z"/></svg>555 014 2318</p>
      <p><svg width="8" height="8" viewBox="0 0 24 24"><path fill="#e3111b" d="M2 5h20v14H2zm2 2v.5l8 5 8-5V7z"/></svg>info@shine4all.com</p>
    </div>
    <div class="faq">
      <h4>FAQ's</h4>
      <ul>
        <li>What sizes of dumpster do we offer?</li>
        <li>How much does a dumpster cost?</li>
        <li>How much can a dumpster hold?</li>
        <li>How long can I keep the dumpster?</li>
      </ul>
      <a class="more" href="#">More FAQ's</a>
    </div>
    <div class="footer-brand"><span class="brand-dot"></span>Shine4All</div>
  </div>
</footer>
<div class="bottom-bar">
  <div class="wrap">
    <span>© 2020 Shine4All. All Rights Reserved.</span>
    <div class="social"><span></span><span></span><span></span></div>
  </div>
</div>

</body>
</html>
```